City department needs a bold and eye-catching poster design.

We need a poster to promote a survey targeting youth and young adults from 14-29 yr olds in the city of Strathcona County. We want poster designs that are bold, provocative and colourful. We want to poster to be a bright piece of art on the wall. See images attached. REQUIRED COPY: "Need something? We're listening" OR "Have Ideas? We're listening" OR "Your Wish? We're listening"

Target Market(s)

Youth, 14-29 yr olds

Industry/Entity Type

Government

Font styles to use
Sans Serif

Requirements
Must have
• REQUIRED COPY: Need something? We're listening"

```html
<!DOCTYPE html>
<html lang="en">
<head>
<meta charset="UTF-8">
<title>Have Ideas? We're Listening</title>
<link rel="stylesheet" href="https://fonts.googleapis.com/css2?family=Montserrat:wght@800&display=swap">
<style>
  :root {
    --bg-deep: #0d171e;
    --bg-mid: #14222b;
    --ink: #ededed;
    --coral: #e8564c;
    --sun: #f0b323;
    --olive: #a8a853;
    --teal: #5b8590;
    --plum: #a94a7d;
    --paper: #ececec;
  }
  * { margin: 0; padding: 0; box-sizing: border-box; }
  html, body {
    width: 800px;
    height: 1200px;
    overflow: hidden;
    background: var(--bg-deep);
  }
  .poster {
    position: relative;
    width: 800px;
    height: 1200px;
    background: radial-gradient(ellipse at 50% 40%, var(--bg-mid) 0%, var(--bg-deep) 75%);
    font-family: "Montserrat", "Helvetica Neue", Arial, sans-serif;
    color: var(--ink);
    overflow: hidden;
  }
  .headline,
  .tagline {
    position: absolute;
    left: 0;
    width: 100%;
    text-align: center;
    font-weight: 800;
    text-transform: uppercase;
    line-height: 1;
  }
  .headline {
    top: 30px;
    font-size: 104px;
    letter-spacing: -1px;
  }
  .tagline {
    top: 1086px;
    font-size: 77px;
    letter-spacing: -0.5px;
  }
  .bulb-art {
    position: absolute;
    left: 64px;
    top: 152px;
    width: 650px;
    height: 900px;
    border-radius: 46% 46% 30% 30% / 40% 40% 20% 20%;
    background:
      linear-gradient(180deg,
        var(--paper) 0%,
        var(--sun) 14%,
        var(--coral) 28%,
        var(--teal) 40%,
        var(--olive) 50%,
        var(--paper) 60%,
        var(--plum) 70%,
        var(--teal) 78%,
        var(--coral) 86%,
        var(--sun) 93%,
        var(--coral) 100%);
    opacity: 0.85;
  }
</style>
</head>
<body>
  <main class="poster">
    <h1 class="headline">Have Ideas?</h1>
    <div class="bulb-art" role="img" aria-label="Light bulb formed from flowing ribbons of coral, yellow, white, olive, teal and plum paper streaming to the left, above a striped coral, white and yellow base"></div>
    <p class="tagline">We’re Listening</p>
  </main>
</body>
</html>
```